Need a landing page design.

We are currently trying to develop a landing page for our www.brightoakwellness.example website.

Objective: To peak a level of interest in Medical Practices to sign up to our program and promote our line of vitamins and supplements. We will be concentrating on email marketing as well as fax or direct mail to drive medical facilities to our landing page.

Page requirements:
1. A slider on the top portion showing our line of products from the brightoakwellness.example website.
2. An "about us" area to explain who we are and what we offer.
3. An area for a grid so that we can show potential earnings for the practice as part of our program.
4. A Testimonial area for a couple of testimonials
5. A scroll area where they can see our contract
6. A lead capture area where they can input their contact information so we may gather it and contact them back to explain the program. In this area I need the following fields: Name of Practice; Contact name; Email address; Phone Number; Area of Medical Discipline; Number of patients per day.
7. A nice clean contact us area

Other than these main requirements the rest is up to you.

Goal: Entice Medical practices to use our FREE service to increase revenue for their offices while helping their patients save money on their supplements.

Key Factors for the Medical facility to know: Free to sign up, no inventory carrying costs. Simple backend sales area to process orders. We handle all shipping and customer service.

Thank you

Target Market(s)

Medical Facilities, mainly office managers and docotors

Industry/Entity Type

Marketing

Requirements
Must have
• Professional design as we are dealing with the medical field.

```html
<!DOCTYPE html>
<html lang="en">
<head>
<meta charset="utf-8">
<title>Bright Oak Wellness – Practice Program</title>
<link href="https://fonts.googleapis.com/css2?family=Cabin:wght@400;500;600;700&family=Lato:ital,wght@0,400;0,700;1,400&display=swap" rel="stylesheet">
<style>
:root{
  --teal:#4fc3cf;
  --teal-dark:#3aaab8;
  --brown:#5a3d2b;
  --brown-dark:#3a2418;
  --ink:#4a3a30;
  --text:#6b6b6b;
  --line:#dedede;
  --bg:#ffffff;
  --band:#ececec;
  --star:#f59a1c;
}
*{box-sizing:border-box;margin:0;padding:0}
html,body{width:754px;height:1200px;overflow:hidden;background:var(--bg)}
body{position:relative;font-family:"Lato",sans-serif;color:var(--text)}
.abs{position:absolute}
.top-rule{left:0;top:0;width:754px;height:3px;background:var(--brown)}
.band{left:0;top:84px;width:754px;height:198px;background:linear-gradient(#fff,var(--band) 30%)}
.account-tab{left:505px;top:0;width:193px;height:32px;background:var(--brown);border-radius:0 0 6px 6px;color:#fff;font-size:9px;display:flex;align-items:center;justify-content:space-around;padding:0 10px;font-family:"Cabin",sans-serif}
.account-tab span{display:flex;align-items:center;gap:3px}
.brand{left:62px;top:14px;width:160px;height:72px;display:flex;align-items:center;gap:6px}
.brand-dot{width:22px;height:22px;border-radius:50%;background:var(--teal);flex:none}
.brand-name{font-family:"Cabin",sans-serif;font-weight:600;font-size:14px;color:var(--teal)}
.phone{left:570px;top:40px;width:123px;text-align:right;font-family:"Cabin",sans-serif;font-size:17px;color:var(--teal);display:flex;align-items:center;justify-content:flex-end;gap:4px}
.search{left:531px;top:66px;width:162px;height:19px;border:1px solid #ccc;border-radius:10px;background:#fff;font-size:7px;font-style:italic;color:#999;padding:5px 8px}
.search svg{position:absolute;right:7px;top:4px}
.nav{left:61px;top:92px;width:632px;height:34px;background:linear-gradient(var(--teal),var(--teal-dark));display:flex;border-top:1px solid #7fd6df}
.nav a{color:#fff;text-decoration:none;font-family:"Cabin",sans-serif;font-size:11px;display:flex;align-items:center;justify-content:center;border-right:1px solid #2f98a5}
.slider{left:61px;top:126px;width:632px;height:216px;background:radial-gradient(ellipse at 60% 40%,#f46a3c,#d8321f 55%,#a81810);overflow:hidden}
.slider .kicker{position:absolute;left:40px;top:56px;color:#fff;font-family:"Cabin",sans-serif;font-size:15px}
.slider h1{position:absolute;left:40px;top:72px;color:#fff;font-family:"Cabin",sans-serif;font-weight:700;font-size:22px;letter-spacing:.2px}
.slider p{position:absolute;left:42px;top:103px;width:230px;color:#fff;font-size:8px;line-height:13px}
.slider .product{position:absolute;left:424px;top:30px;width:110px;height:145px;border-radius:14px;background:linear-gradient(90deg,#c9d3d8,#f2f5f6 40%,#8aa0b0)}
.dots{position:absolute;left:297px;top:198px;display:flex;gap:3px}
.dots i{width:8px;height:8px;border-radius:50%;background:#fff;opacity:.9}
h2.section{font-family:"Cabin",sans-serif;font-weight:400;color:var(--ink);font-size:17px}
.welcome{left:61px;top:366px;width:425px}
.welcome .lead{font-size:9.5px;color:#444;margin-top:6px}
.welcome .body{font-size:7.5px;line-height:15px;margin-top:5px}
.col{width:215px;font-size:7.5px;line-height:15px;white-space:nowrap}
.col h3{font-family:"Cabin",sans-serif;font-weight:400;color:var(--teal);font-size:13px;margin-bottom:4px}
.divider{left:61px;top:558px;width:422px;height:1px;background:var(--line)}
.card{top:602px;width:134px;height:167px;border:1px solid var(--line);border-radius:3px;overflow:hidden;background:#fff}
.card .pic{height:110px;display:flex;align-items:center;justify-content:center}
.card .pic div{width:44px;height:88px;border-radius:8px}
.card .info{position:absolute;left:0;top:110px;width:100%;height:57px;background:var(--teal);color:#fff;padding:7px 9px}
.card .name{font-family:"Cabin",sans-serif;font-size:10px;display:flex;align-items:center;gap:6px}
.stars{color:var(--star);font-size:9px;letter-spacing:-1px}
.card .price{font-size:6.5px;line-height:12px;margin-top:2px}
.card .cart{position:absolute;right:5px;bottom:9px;background:var(--brown-dark);color:#fff;font-size:6.5px;padding:4px 6px;border-radius:3px}
.testi{top:819px;width:196px;height:125px;border:1px solid var(--line);border-radius:5px;background:#fff;box-shadow:0 1px 3px rgba(0,0,0,.06);padding:15px 17px}
.testi .avatar{float:left;width:50px;height:46px;margin:0 8px 2px 0}
.testi .quote{font-size:7.5px;font-style:italic;color:#999;line-height:15.5px}
.testi .by{clear:both;font-size:8.5px;color:#333;padding-top:6px}
.panel{left:504px;width:189px;border:1px solid var(--line);background:#fff}
.panel-head{height:31px;font-family:"Cabin",sans-serif;font-size:14px;display:flex;align-items:center;padding-left:15px}
.form .panel-head{background:var(--teal);color:#fff}
.field{position:absolute;left:15px;width:158px;height:19px;border:1px solid #ccc;border-radius:2px;font-size:7.5px;color:#666;padding:5px 8px;background:#fff}
.submit{position:absolute;left:103px;top:208px;width:71px;height:19px;background:var(--brown-dark);color:#fff;font-family:"Cabin",sans-serif;font-weight:700;font-size:7.5px;border-radius:3px;display:flex;align-items:center;justify-content:center}
.contract .panel-head{color:var(--ink);background:linear-gradient(#fff,#f3f3f3);border-bottom:1px solid var(--line)}
.scroll-btn{position:absolute;right:12px;top:8px;width:20px;height:20px;border-radius:50%;background:var(--teal)}
.partner{position:absolute;left:0;right:0;top:48px;display:flex;align-items:center;justify-content:center;gap:8px;font-family:"Cabin",sans-serif;font-size:14px;color:var(--ink)}
.partner i{width:24px;height:24px;border-radius:50%;background:#8db04a}
.earn .panel-head{height:52px;background:linear-gradient(#8a6a50,var(--brown));color:#fff;font-weight:400;font-size:14px;line-height:18px;padding-left:18px}
.earn .thumb{position:absolute;left:16px;top:63px;width:65px;height:55px;background:linear-gradient(#6ab3e0,#1d5e9a);border-radius:3px}
.earn .copy{font-size:7.5px;line-height:14px;color:#666;padding:13px 17px 0}
.earn .copy b{font-family:"Cabin",sans-serif;font-weight:400;font-size:11px;color:#333}
.earn .more{font-family:"Cabin",sans-serif;font-weight:700;font-size:7.5px;color:var(--brown-dark);padding:10px 20px}
.footer{left:0;top:978px;width:754px;height:222px;background:linear-gradient(var(--brown),var(--brown-dark));color:#fff}
.fcol{position:absolute;top:28px}
.fcol h4{font-family:"Cabin",sans-serif;font-weight:400;font-size:13px;margin-bottom:8px}
.fcol li{list-style:none;font-size:7.5px;line-height:15px;padding-left:3px}
.social{display:flex;gap:4px;padding-left:3px}
.social i{width:20px;height:20px;border-radius:50%;background:#fff}
.frule{position:absolute;left:61px;top:174px;width:632px;height:1px;background:#7a5c48}
.copyright{position:absolute;left:60px;top:188px;font-size:7.5px;color:#b9a393}
</style>
</head>
<body>
<div class="abs top-rule"></div>
<div class="abs band"></div>

<header>
  <div class="abs brand"><span class="brand-dot"></span><span class="brand-name">Bright Oak Wellness</span></div>
  <div class="abs account-tab">
    <span><svg width="10" height="10" viewBox="0 0 10 10"><circle cx="5" cy="3" r="2.5" fill="#fff"/><path d="M0 10a5 4 0 0 1 10 0z" fill="#fff"/></svg>My Account</span>
    <span><svg width="12" height="10" viewBox="0 0 12 10"><path d="M0 1h2l2 6h6l1.5-4.5H3" fill="none" stroke="#fff"/><circle cx="5" cy="9" r="1" fill="#fff"/><circle cx="9" cy="9" r="1" fill="#fff"/></svg>Checkout</span>
    <span><svg width="9" height="10" viewBox="0 0 9 10"><path d="M3 0h1.5v5l4 1-1 4H3L1 6z" fill="#fff"/></svg>Login</span>
  </div>
  <div class="abs phone"><svg width="14" height="14" viewBox="0 0 14 14"><path d="M3 1l3 3-1.5 2a8 8 0 0 0 3.5 3.5L10 8l3 3-2 2C5 12 2 9 1 3z" fill="var(--teal)"/></svg>888.555.0142</div>
  <div class="abs search">Search here..<svg width="10" height="10" viewBox="0 0 10 10"><circle cx="4" cy="4" r="3" fill="none" stroke="#555" stroke-width="1.5"/><path d="M6.5 6.5L9.5 9.5" stroke="#555" stroke-width="1.5"/></svg></div>
  <nav class="abs nav">
    <a style="width:69px">HOME</a><a style="width:82px">ABOUT US</a><a style="width:85px">PRODUCTS</a><a style="width:94px">CONTACT US</a><a style="width:70px">SIGN IN</a>
  </nav>
</header>

<section class="abs slider">
  <div class="kicker">SMART AND SUSTAINABLE</div>
  <h1>INCREASE SEX DRIVE &amp; STAMINA</h1>
  <p>Nunc tempus felis vitae urna. Vivamus porttitor, g, purus nisi eleifend libero, a tempus libero lectus feugiat felis.</p>
  <div class="product" role="img" aria-label="Supplement tub product photo"></div>
  <div class="dots"><i></i><i></i><i></i><i></i></div>
</section>

<section class="abs welcome">
  <h2 class="section">Welcome to Our Website Mainpage</h2>
  <p class="lead">Nunc tempus felis vitae urna Vivamus porttitor purus nisi eleifend libero, a tempus</p>
  <p class="body">Phasellus felis dolor, scelerisque a, tempus eget, lobortis id, libero. Donec scelerisque leo ac risus. Praesent sit amet est.<br>In dictum, dolor eu dictum porttitor, enim felis viverra mi, eget luctus massa purus quis odio.</p>
</section>
<div class="abs col" style="left:60px;top:458px"><h3>Who we are</h3>Duis tincidunt lectus quis dui viverra vestibulum.<br>Suspendisse vulputate aliquam dui. Nulla elementum<br>dui ut augue. Aliquam vehicula mi at mauris.<br>Maecenas placerat nisl at</div>
<div class="abs col" style="left:278px;top:458px"><h3>What we offer</h3>Duis tincidunt lectus quis dui viverra vestibulum.<br>Suspendisse vulputate aliquam dui. Nulla elementum<br>dui ut augue. Aliquam vehicula mi at mauris.<br>Maecenas placerat nisl at</div>
<div class="abs divider"></div>

<h2 class="abs section" style="left:61px;top:578px">Latest Products</h2>
<div class="abs card" style="left:62px"><div class="pic"><div role="img" aria-label="Supplement jar photo" style="background:linear-gradient(90deg,#9a9a92,#e6e2d6,#8a8478)"></div></div><div class="info"><div class="name">Product Name <span class="stars">★★★★</span></div><div class="price">Easy Auto Ship: $33.25<br>Regular Price: $39.95</div><span class="cart">Add to Cart</span></div></div>
<div class="abs card" style="left:205px"><div class="pic"><div role="img" aria-label="Blue supplement bottle photo" style="background:linear-gradient(90deg,#1d6aa8,#63c0ec,#1d5e9a)"></div></div><div class="info"><div class="name">Product Name <span class="stars">★★★★</span></div><div class="price">Easy Auto Ship: $33.25<br>Regular Price: $39.95</div><span class="cart">Add to Cart</span></div></div>
<div class="abs card" style="left:347px"><div class="pic"><div role="img" aria-label="Dark supplement bottle photo" style="background:linear-gradient(90deg,#1a1c28,#55586a,#15161f)"></div></div><div class="info"><div class="name">Product Name <span class="stars">★★★★</span></div><div class="price">Easy Auto Ship: $33.25<br>Regular Price: $39.95</div><span class="cart">Add to Cart</span></div></div>

<h2 class="abs section" style="left:61px;top:792px">Testimonials</h2>
<div class="abs testi" style="left:61px"><div class="avatar" role="img" aria-label="Customer portrait" style="background:linear-gradient(#c9a88a,#8a6a56)"></div><p class="quote">Duis tincidunt lectus quis dui viverra vestibulum pendisse vulputa aliquam metus eget imperdiet vitae, tellus. Sed odio est, auctor ac, sollicitudin in, consequat vitae.</p><p class="by">By Author Name</p></div>
<div class="abs testi" style="left:273px"><div class="avatar" role="img" aria-label="Customer portrait" style="background:linear-gradient(#a8866c,#5a3c2c)"></div><p class="quote">Duis tincidunt lectus quis dui viverra vestibulum pendisse vulputa aliquam metus eget imperdiet vitae, tellus. Sed odio est, auctor ac, sollicitudin in, consequat vitae.</p><p class="by">By Author Name</p></div>

<aside>
  <form class="abs panel form" style="top:362px;height:242px">
    <div class="panel-head">Fill Our Contact Form</div>
    <div class="field" style="top:45px">Name of Practice</div>
    <div class="field" style="top:72px">Contact name</div>
    <div class="field" style="top:99px">Email address</div>
    <div class="field" style="top:126px">Phone Number</div>
    <div class="field" style="top:153px">Area of Medical Discipline</div>
    <div class="field" style="top:179px">Number of patients per day<svg style="position:absolute;right:6px;top:7px" width="7" height="5" viewBox="0 0 7 5"><path d="M0 0h7L3.5 5z" fill="#222"/></svg></div>
    <div class="submit">SUBMIT NOW</div>
  </form>

  <section class="abs panel contract" style="top:615px;height:119px">
    <div class="panel-head">Our Contract</div>
    <div class="scroll-btn"><svg width="20" height="20" viewBox="0 0 20 20"><path d="M8 6l-4 4 4 4M12 6l4 4-4 4" fill="none" stroke="#fff" stroke-width="1.5"/></svg></div>
    <div class="partner"><i></i>Green Step Health</div>
  </section>

  <section class="abs panel earn" style="top:745px;height:199px">
    <div class="panel-head">Potential Earnings for<br>the Practice</div>
    <div class="thumb" role="img" aria-label="Supplement bottles photo"></div>
    <div class="copy"><div style="padding-left:73px"><b>Duis tincidunt</b><br>quis dui viverra<br>vestibulum. Suspend<br>isse vulputate aliquam</div>quis dui viverra vestibulum. Suspend isse vulputate aliquam dui. Nulla elementum dui ut augue Aliquam</div>
    <div class="more">LEARN MORE</div>
  </section>
</aside>

<footer class="abs footer">
  <div class="fcol" style="left:64px"><h4>Quick Links</h4><ul><li>Home</li><li>About Us</li><li>Products</li><li>Contact Us</li><li>Become an Affiliate</li><li>Become a Reseller</li></ul></div>
  <div class="fcol" style="left:183px"><h4>Terms and Conditions</h4><ul><li>Privacy Policy</li><li>Return Policy</li><li>Terms and Conditions</li><li>Contact Us</li></ul></div>
  <div class="fcol" style="left:353px"><h4>Contact Information</h4><ul><li style="font-size:9px">Bright Oak Wellness</li><li>42 Harbor Lane Suite 5</li><li>Portland 97201 OR</li><li>Phone no. <span style="font-size:10px">888-555-0142</span></li><li>Email add: info@brightoakwellness.example</li></ul></div>
  <div class="fcol" style="left:525px"><h4>Get Connected</h4><div class="social" aria-label="Social profiles"><i></i><i></i><i></i><i></i></div></div>
  <div class="frule"></div>
  <p class="copyright">Copyright © 2013 Company Name.&nbsp; All right reserved.</p>
</footer>
</body>
</html>
```